Website for new dental office

I am Dr. Colin Marsh and am building a new dental practice. I specialize in general dentistry. I am young and have a higher end dental practice incorporating very new technologies and would like my website to reflect that. As many dental patients are older, the website must be very easy to navigate. I would like patients to be able to request appointments, and will eventually add on patient information forms (the health history, etc, that you normally fill out in the practice) from my practice management software, so leave an area for that.

Industry/Entity Type

Building

```html
<!DOCTYPE html>
<html lang="en">
<head>
<meta charset="utf-8">
<title>Dr. Colin Marsh – General Dentistry</title>
<link href="https://fonts.googleapis.com/css2?family=Arimo:wght@400;700&display=swap" rel="stylesheet">
<style>
:root{
  --teal:#5ec3d6;
  --teal-dark:#3fa8bf;
  --mint:#8fd9c4;
  --lime:#8ed63c;
  --yellow:#f7c83a;
  --ink:#3a3a3a;
  --grey:#8a8a8a;
  --line:#e4e4e4;
  --white:#ffffff;
  --link:#3fa8c2;
}
*{margin:0;padding:0;box-sizing:border-box}
html,body{width:820px;height:1200px;overflow:hidden;background:var(--white);font-family:"Arimo",Arial,sans-serif;color:var(--ink)}
.page{position:relative;width:820px;height:1200px}
.abs{position:absolute}

/* header */
.header{left:0;top:0;width:820px;height:160px;background:linear-gradient(180deg,var(--teal) 0%,#7fd0dd 100%)}
.logo{left:37px;top:0;width:244px;height:104px;background:var(--mint);display:flex;align-items:center;justify-content:center;color:var(--white);font-size:32px;letter-spacing:-0.5px}
.logo small{font-size:19px;margin-right:6px;font-weight:700}
.nav{left:411px;top:0;display:flex;height:47px}
.nav a{color:var(--white);text-decoration:none;font-size:12px;font-weight:700;padding:15px 7px 0;height:47px}
.nav a.current{background:var(--teal-dark);border-radius:0 0 6px 6px;padding:15px 8px 0}
.call{left:470px;top:70px;color:var(--white);font-size:20px;display:flex;align-items:center;gap:8px}

/* slider */
.slider{left:36px;top:124px;width:744px;height:340px;background:var(--white);box-shadow:0 6px 14px rgba(0,0,0,.12)}
.tiles{left:11px;top:13px;width:310px;height:310px;display:grid;grid-template-columns:repeat(3,1fr);gap:3px}
.tile{background:linear-gradient(160deg,#f1c7b0,#d98b86)}
.tile:nth-child(2n){background:linear-gradient(160deg,#e9b89f,#c9706f)}
.slide-title{left:351px;top:36px;font-size:24px;font-weight:700;color:#7d7d7d}
.slide-title span{color:var(--lime)}
.rule{height:1px;background:var(--line)}
.slide-lead{left:351px;top:97px;width:290px;font-size:16px;line-height:23px;color:#9a9a9a}
.slide-body{left:351px;top:154px;width:290px;font-size:10.5px;line-height:15px;color:#aaa}
.read{left:547px;top:247px;font-size:14px;color:var(--ink);display:flex;align-items:center;gap:5px}
.arrow{display:inline-block;width:9px;height:9px;border-radius:50%;background:#9a9a9a;position:relative}
.arrow:after{content:"";position:absolute;left:3px;top:2.5px;border-left:4px solid #fff;border-top:2px solid transparent;border-bottom:2px solid transparent}
.dots{left:350px;top:298px;display:flex;gap:2px}
.dots i{width:11px;height:11px;border-radius:50%;border:1px solid #ccc;display:block}
.dots i.on{background:#ccc;box-shadow:inset 0 0 0 2px #fff}

/* search */
.search{left:42px;top:488px;display:flex;align-items:center}
.search-label{font-size:21px;color:#555;margin-left:10px;white-space:nowrap}
.search-input{left:403px;top:493px;width:268px;height:23px;border-radius:12px;background:#eeeeee}
.search-btn{left:677px;top:493px;width:71px;height:23px;border-radius:12px;background:var(--yellow);color:#fff;font-size:12px;display:flex;align-items:center;justify-content:center}

/* services band */
.band{left:0;top:539px;width:820px;height:297px;border-top:6px solid #a6e39a;background:linear-gradient(180deg,#5ec3d6 0%,#8edbc4 100%)}
.service{top:0;width:182px;text-align:center;color:var(--white)}
.service h3{font-size:19px;font-weight:700;margin-top:30px;white-space:nowrap}
.badge{width:117px;height:117px;border-radius:50%;background:var(--white);margin:16px auto 0;display:flex;align-items:center;justify-content:center}
.badge-art{width:99px;height:99px;border-radius:50%;background:linear-gradient(160deg,#7fd1d8,#9ddfcd)}
.service p{font-size:9.5px;line-height:12px;margin:13px auto 0;width:124px;height:36px}
.pill{display:inline-block;margin-top:16px;width:88px;height:24px;border-radius:12px;background:rgba(255,255,255,.3);font-size:9px;line-height:24px}
.divider{top:30px;width:0;height:245px;border-left:1px dotted rgba(255,255,255,.8)}
.top-btn{left:782px;top:779px;width:40px;height:40px;border-radius:50%;background:var(--white);color:var(--teal);font-size:12px;display:flex;align-items:center;justify-content:center}

/* info columns */
.col{top:866px;width:150px}
.col h4{font-size:15px;font-weight:400;line-height:20px;color:var(--ink)}
.col p{font-size:10px;line-height:14.5px;color:#888;margin-top:10px}
.more{font-size:13px;margin-top:14px;display:flex;align-items:center;gap:5px}
.links a{display:block;font-size:10px;color:var(--link);margin-top:6px;text-decoration:underline}
.address{left:607px;top:867px;width:168px;height:138px;background:#f6f6f6;border:1px solid #e8e8e8;box-shadow:0 1px 3px rgba(0,0,0,.08);padding:26px 0 0 27px;font-size:10px;line-height:15px;color:#777;font-style:normal}
.address a{color:var(--link);display:block;margin-top:12px;text-decoration:underline}

/* footer */
.hr{left:60px;width:718px;height:1px;background:#ececec}
.foot-nav{left:60px;top:1084px;display:flex;font-size:9.5px;color:#888}
.foot-nav span{padding:0 10px;border-left:1px solid #ddd}
.foot-nav span:first-child{padding-left:0;border:0;text-decoration:underline}
.vline{left:463px;top:1064px;width:1px;height:46px;background:#e2e2e2}
.social{top:1068px;display:flex;align-items:center;gap:9px;color:var(--link)}
.social-mark{width:40px;height:40px;border-radius:4px}
.social small{display:block;font-size:10.5px}
.social b{display:block;font-size:16px;font-weight:400}
.copy{left:60px;top:1142px;font-size:9px;color:#888}
</style>
</head>
<body>
<div class="page">

  <header class="header abs"></header>
  <div class="logo abs"><small>Dr.</small>Colin Marsh</div>
  <nav class="nav abs">
    <a class="current">HOME</a><a>BLOG</a><a>OUR STAFF</a><a>GALLERY</a><a>PRICES</a><a>CONTACTS</a>
  </nav>
  <div class="call abs">
    <svg width="14" height="16" viewBox="0 0 14 16"><path d="M3 1 L6 4 L4.5 6 Q6 10 9 12 L11 10.5 L13.5 13 L11.5 15.5 Q2 13 1 3 Z" fill="#2f3b40"/></svg>
    Call Toll Free:
  </div>

  <section class="slider abs">
    <div class="tiles abs" role="img" aria-label="Grid of nine smiling patient photographs">
      <div class="tile"></div><div class="tile"></div><div class="tile"></div>
      <div class="tile"></div><div class="tile"></div><div class="tile"></div>
      <div class="tile"></div><div class="tile"></div><div class="tile"></div>
    </div>
    <h2 class="slide-title abs">General <span>Dentistry</span></h2>
    <div class="rule abs" style="left:351px;top:79px;width:276px"></div>
    <p class="slide-lead abs">Gentle family care backed by the newest dental technology.</p>
    <p class="slide-body abs">Digital x-rays, same-day care and clear advice for every age. Request a visit online in a few easy steps and we will call you back.</p>
    <div class="read abs">Read More <span class="arrow"></span></div>
    <div class="rule abs" style="left:351px;top:283px;width:276px"></div>
    <div class="dots abs"><i></i><i></i><i class="on"></i></div>
  </section>

  <div class="search abs">
    <svg width="40" height="36" viewBox="0 0 40 36"><circle cx="14" cy="14" r="10" fill="none" stroke="#c8c8c8" stroke-width="4"/><path d="M21 21 L33 32" stroke="#c8c8c8" stroke-width="6" stroke-linecap="round"/></svg>
    <span class="search-label"><b>Search</b> for articles on the site:</span>
  </div>
  <div class="search-input abs"></div>
  <div class="search-btn abs">Search</div>

  <section class="band abs">
    <div class="service abs" style="left:33px">
      <h3>Our Profile</h3>
      <div class="badge"><div class="badge-art" role="img" aria-label="Tooth illustration"></div></div>
      <p>Modern general dentistry for the whole family.</p>
      <span class="pill">learn more</span>
    </div>
    <div class="divider abs" style="left:213px"></div>
    <div class="service abs" style="left:213px">
      <h3>Appointments</h3>
      <div class="badge"><div class="badge-art" role="img" aria-label="Calendar illustration"></div></div>
      <p>Pick a day and time and we will confirm by phone.</p>
      <span class="pill">request</span>
    </div>
    <div class="divider abs" style="left:395px"></div>
    <div class="service abs" style="left:394px">
      <h3>Patient Forms</h3>
      <div class="badge"><div class="badge-art" role="img" aria-label="Clipboard with forms illustration"></div></div>
      <p>Health history and new patient forms to fill in.</p>
      <span class="pill">open forms</span>
    </div>
    <div class="divider abs" style="left:576px"></div>
    <div class="service abs" style="left:576px">
      <h3>Emergency</h3>
      <div class="badge"><div class="badge-art" role="img" aria-label="First aid kit illustration"></div></div>
      <p>Tooth pain or injury? Call us for same-day help.</p>
      <span class="pill">learn more</span>
    </div>
  </section>
  <div class="top-btn abs">top</div>

  <div class="col abs" style="left:60px">
    <h4>Only Professional Services</h4>
    <p>Check-ups, cleanings, fillings and crowns done with the latest digital tools for quick, comfortable visits.</p>
    <div class="more">Learn More <span class="arrow"></span></div>
  </div>
  <div class="col abs" style="left:241px;width:160px">
    <h4>Patient Support and Consultations</h4>
    <p>Questions about treatment or insurance? Our team explains every step clearly and helps you plan each visit.</p>
    <div class="more">Learn More <span class="arrow"></span></div>
  </div>
  <div class="col links abs" style="left:452px">
    <h4>Useful Links</h4>
    <div style="margin-top:6px">
      <a>Request an appointment</a><a>New patient forms</a><a>Insurance and fees</a><a>Directions</a>
    </div>
  </div>
  <address class="address abs">
    Bright Arc<br>14 Alder Row Ste 210<br>Fairhaven<br>OR 97120-4410
    <a>hello@brightarc-dental.com</a>
  </address>
  <svg class="abs" style="left:741px;top:853px" width="16" height="32" viewBox="0 0 16 32"><path d="M5 28 V6 Q5 2 8.5 2 Q12 2 12 6 V24 Q12 27 9 27 Q7 27 7 24 V9" fill="none" stroke="#b5b5b5" stroke-width="1.5"/></svg>

  <div class="hr abs" style="top:1057px"></div>
  <div class="foot-nav abs"><span>HOME</span><span>BLOG</span><span>OUR STAFF</span><span>GALLERY</span><span>PRICES</span><span>CONTACTS</span></div>
  <div class="vline abs"></div>
  <div class="social abs" style="left:483px">
    <span class="social-mark" style="background:#3b5a93"></span>
    <div><small>Follow us on</small><b>Circlebook</b></div>
  </div>
  <div class="social abs" style="left:633px">
    <span class="social-mark" style="background:#3fb6d8"></span>
    <div><small>Follow us on</small><b>Chirper</b></div>
  </div>
  <div class="hr abs" style="top:1122px"></div>
  <div class="copy abs">BRIGHT ARC © 2014 • PRIVACY POLICY</div>

</div>
</body>
</html>
```